Akademie für Wahrnehmungspflege
Zielgruppe
Ich biete die beiden Seminare 'Kraftquell im Jahreslauf' und 'Feinsinn im Wochenlauf' an. Die Zielgruppe sind spirituell interessierte Leute.
Aufgabenstellung
Die Anzeige sollte mehr oder weniger mit den Farben meiner Webseite übereinstimmen (www.am-ruhepol.ch).
Grösse der Anzeige:
breit: 121mm
hoch: 124mm
Die Anzeige sollte mein persönliches Bild und das Logo enthalten.
Text:
Feinsinn im Wochenlauf:
Seminare zur Förderung Ihrer Intuition. Entdecken Sie Ihre eigene Medialität und lernen Sie diese gezielt im Alltag einzusetzen.
26./27. August 2017
11./12. November 2017
Kraftquell im Jahreslauf:
Seminare für energetisches Heilen. Lernen Sie sich und andere Menschen energetisch zu begleiten.
16./17. September 2017
9./10. Dezember 2017
2 für 1 - Aktion:
Kommen Sie zu zweit und bezahlen Sie nur für eine Person
(gültig bis Ende 2017)
Webseite:
www.am-ruhepol.ch
Seminarort: Grünmattenhof, 3127 Auenried, Schweiz

```html
<!DOCTYPE html>
<html lang="de">
<head>
<meta charset="utf-8">
<title>Akademie für Wahrnehmungspflege – Ausbildungen</title>
<link rel="stylesheet" href="https://fonts.googleapis.com/css2?family=Fira+Sans+Condensed:wght@400;500;600&display=swap">
<style>
  :root {
    --brand-blue: #3f7bc3;
    --brand-orange: #e8742b;
    --paper: #ffffff;
    --ink: #2e2e2e;
    --photo-light: #d9d9d9;
    --photo-dark: #6b6b6b;
  }
  * { margin: 0; padding: 0; box-sizing: border-box; }
  html, body { width: 1153px; height: 1200px; overflow: hidden; background: #fff; }
  body { font-family: "Fira Sans Condensed", "Arial Narrow", sans-serif; color: var(--ink); }
  .ad { position: relative; width: 1153px; height: 1200px; background: var(--brand-blue); overflow: hidden; }
  .paper-shapes { position: absolute; inset: 0; }
  .brand { position: absolute; left: 290px; top: 96px; width: 600px; display: flex; align-items: center; justify-content: center; gap: 14px; }
  .brand-dot { width: 30px; height: 30px; border-radius: 50%; background: var(--brand-blue); flex: none; }
  .brand-name { font-size: 36px; font-weight: 500; color: var(--brand-orange); line-height: 1.1; white-space: nowrap; }
  .section-label { position: absolute; left: 52px; top: 246px; font-size: 24px; font-weight: 600; letter-spacing: 1px; color: var(--paper); }
  .portrait { position: absolute; left: 9px; top: 344px; width: 272px; height: 272px; border-radius: 50%;
    background: radial-gradient(circle at 55% 40%, var(--photo-light), var(--photo-dark) 85%); }
  .portrait-caption { position: absolute; left: 0; top: 675px; width: 290px; text-align: center; font-size: 25px; }
  .course { position: absolute; left: 310px; width: 790px; }
  .course-title { font-size: 60px; font-weight: 500; color: var(--brand-orange); line-height: 1; white-space: nowrap; }
  .course-text { margin-left: 32px; margin-top: 12px; font-size: 31px; line-height: 42px; }
  .course-dates { margin-left: 32px; margin-top: 8px; font-size: 31px; font-weight: 600; display: flex; gap: 30px; }
  .course-dates li { list-style: none; display: flex; align-items: center; }
  .course-dates li::before { content: ""; width: 20px; height: 20px; border-radius: 50%; background: var(--brand-orange); margin-right: 10px; }
  .course-rule { margin-left: 22px; margin-top: 18px; width: 758px; height: 3px; background: var(--brand-orange); }
  .course--intuition { top: 322px; }
  .course--energy { top: 617px; }
  .offer-badge { position: absolute; left: 47px; top: 870px; width: 262px; height: 48px; border-radius: 8px;
    background: var(--brand-orange); color: var(--paper); font-size: 30px; font-weight: 600; line-height: 48px; text-align: center; }
  .offer-text { position: absolute; left: 342px; top: 866px; font-size: 31px; line-height: 38px; }
  .offer-note { font-size: 20px; line-height: 30px; }
  .venue { position: absolute; left: 342px; top: 1002px; font-size: 31px; white-space: nowrap; }
  .venue-label { color: var(--brand-orange); font-weight: 600; }
  .website { position: absolute; left: 0; top: 1088px; width: 100%; text-align: center; font-size: 54px; font-weight: 500; color: var(--paper); }
</style>
</head>
<body>
<div class="ad">
  <svg class="paper-shapes" width="1153" height="1200" viewBox="0 0 1153 1200" aria-hidden="true">
    <polygon fill="#ffffff" points="272,0 918,0 914,40 920,90 910,140 916,190 905,228 860,238 800,232 740,244 680,236 620,246 560,238 500,247 440,236 380,244 320,234 284,240 276,190 270,140 278,90 268,40"/>
    <polygon fill="#ffffff" points="19,296 80,288 160,298 240,286 330,294 420,284 520,296 620,286 720,296 820,284 920,294 1010,286 1080,296 1134,290 1134,1058 1070,1066 980,1054 880,1068 780,1056 680,1066 580,1054 480,1068 380,1056 280,1066 180,1054 90,1066 19,1058"/>
  </svg>

  <div class="brand">
    <span class="brand-dot"></span>
    <span class="brand-name">Akademie für Wahrnehmungspflege</span>
  </div>

  <div class="section-label">AUSBILDUNGEN</div>

  <div class="portrait" role="img" aria-label="Porträtfoto des Seminarleiters in Schwarzweiss"></div>
  <div class="portrait-caption">Lukas Berthoud</div>

  <section class="course course--intuition">
    <h2 class="course-title">„Feinsinn im Wochenlauf“</h2>
    <p class="course-text">Seminare zur Förderung Ihrer Intuition. Entde-<br>cken Sie Ihre eigene Medialität und lernen Sie<br>diese gezielt im Alltag einzusetzen.</p>
    <ul class="course-dates"><li>26./27. August 2017</li><li>11./12. November 2017</li></ul>
    <div class="course-rule"></div>
  </section>

  <section class="course course--energy">
    <h2 class="course-title">„Kraftquell im Jahreslauf“</h2>
    <p class="course-text">Seminare für energetisches Heilen. Lernen Sie sich<br>und andere Menschen energetisch zu begleiten.</p>
    <ul class="course-dates"><li>16./17. September 2017</li><li>09./10. Dezember 2017</li></ul>
    <div class="course-rule"></div>
  </section>

  <div class="offer-badge">2 für 1-Aktion:</div>
  <p class="offer-text">Kommen Sie zu zweit und bezahlen<br>Sie nur für eine Person<br><span class="offer-note">(gültig bis Ende 2017)</span></p>

  <p class="venue"><span class="venue-label">Seminarort:</span> Grünmattenhof, 3127 Auenried, Schweiz</p>

  <div class="website">www.am-ruhepol.ch</div>
</div>
</body>
</html>
```